Business Card Design for Online Gift Business

Business card design for a new online Canadian company called "Harlow & Reed Gift Crates" selling modern and luxurious gift boxes for every occasion. Items are sourced locally from talented socially-responsible Canadian artisans. Each gift is elegantly presented in a keepsake wood box to ensure a lasting impression.

Industry/Entity Type

E-Commerce

Contact Information for Business Card

Merin Holloway, Proprietor
Calgary, AB
587-214-3306
www.harlowandreed.ca
hello@harlowandreed.ca

Requirements
Must have
• Gifts from our best, to your best
• Please also include the symbols for Facebook and Instagram
Nice to have
• **I have attached a few samples of background colors and font colors that I like. I hope this helps in a few directions to try.

```html
<!DOCTYPE html>
<html lang="en">
<head>
<meta charset="utf-8">
<title>Harlow &amp; Reed Gift Crates – Business Card</title>
<link href="https://fonts.googleapis.com/css2?family=Arimo:ital,wght@0,400;0,700;1,400&display=swap" rel="stylesheet">
<style>
  :root {
    --backdrop: #e9e6e1;
    --card-white: #fbfbfa;
    --pattern-base: #d4cab9;
    --brand-brown: #4d3727;
    --gold: #b0976b;
    --ink: #2e2e2e;
    --icon-grey: #8c8c8c;
    --band: #3f3f3f;
    --url-light: #ffffff;
  }
  * { margin: 0; padding: 0; box-sizing: border-box; }
  html, body { width: 1200px; height: 960px; overflow: hidden; }
  body {
    position: relative;
    background: var(--backdrop);
    font-family: "Arimo", Arial, sans-serif;
  }
  .card {
    position: absolute;
    left: 270px;
    width: 645px;
    height: 369px;
    overflow: hidden;
    box-shadow: 0 6px 18px rgba(0,0,0,0.18);
  }
  .card--front { top: 83px; }
  .card--back { top: 507px; background: var(--card-white); }

  .front__pattern {
    position: absolute; inset: 0;
    background: radial-gradient(ellipse at 55% 50%, #d9d0c1 0%, var(--pattern-base) 60%, #c9bca6 100%);
  }
  .wordmark {
    position: absolute;
    color: var(--brand-brown);
    font-weight: 400;
    white-space: nowrap;
  }
  .front__wordmark {
    left: 0; right: 0; top: 196px;
    text-align: center;
    font-size: 54px;
    letter-spacing: 1px;
  }
  .front__url {
    position: absolute;
    left: 0; right: 0; top: 337px;
    text-align: center;
    color: var(--url-light);
    font-size: 14px;
    letter-spacing: 3px;
  }

  .back__identity { position: absolute; left: 40px; top: 75px; }
  .back__name { color: var(--gold); font-size: 19px; font-weight: 700; }
  .back__role { color: var(--ink); font-size: 14px; margin-top: 5px; }
  .contact-list {
    position: absolute; left: 40px; top: 148px;
    list-style: none;
    color: var(--ink); font-size: 14px;
  }
  .contact-list li {
    display: flex; align-items: center; gap: 9px;
    height: 19px;
  }
  .contact-list svg { width: 14px; height: 14px; flex: none; fill: var(--icon-grey); }
  .contact-list .accent { color: var(--gold); }
  .back__city {
    position: absolute; left: 40px; top: 246px;
    color: var(--ink); font-size: 14px;
  }
  .back__wordmark {
    left: 370px; top: 90px;
    font-size: 31px;
  }
  .back__band {
    position: absolute; left: 0; right: 0; top: 293px; height: 28px;
    background: var(--band);
  }
  .back__band-accent {
    position: absolute; left: 520px; top: 291px; width: 72px; height: 32px;
    background: linear-gradient(90deg, #e8dcc6, #c9b18a);
    border-radius: 3px;
  }
  .back__tagline {
    position: absolute; left: 40px; top: 336px;
    color: var(--gold); font-size: 13px; font-style: italic;
  }
  .social {
    position: absolute; right: 40px; top: 333px;
    display: flex; gap: 8px;
  }
  .social__badge {
    width: 20px; height: 20px; border-radius: 50%;
    background: var(--icon-grey);
  }
</style>
</head>
<body>
  <section class="card card--front" aria-label="Card front">
    <div class="front__pattern" role="img" aria-label="Repeating maple leaf pattern in tan on warm beige"></div>
    <div class="wordmark front__wordmark">Harlow &amp; Reed</div>
    <div class="front__url">www.harlowandreed.ca</div>
  </section>

  <section class="card card--back" aria-label="Card back">
    <div class="back__identity">
      <div class="back__name">Merin Holloway</div>
      <div class="back__role">Proprietor</div>
    </div>

    <ul class="contact-list">
      <li>
        <svg viewBox="0 0 24 24" aria-hidden="true"><path d="M6.6 10.8a15.1 15.1 0 0 0 6.6 6.6l2.2-2.2a1 1 0 0 1 1-.25 11.4 11.4 0 0 0 3.6.57 1 1 0 0 1 1 1V20a1 1 0 0 1-1 1A17 17 0 0 1 3 4a1 1 0 0 1 1-1h3.5a1 1 0 0 1 1 1c0 1.25.2 2.45.57 3.57a1 1 0 0 1-.25 1z"/></svg>
        587-214-3306
      </li>
      <li>
        <svg viewBox="0 0 24 24" aria-hidden="true"><path d="M2 5h20v14H2zm2 2v.5l8 5 8-5V7zm0 2.8V17h16V9.8l-8 5z"/></svg>
        hello@harlowandreed.ca
      </li>
      <li>
        <svg viewBox="0 0 24 24" aria-hidden="true"><path d="M12 2a10 10 0 1 0 0 20 10 10 0 0 0 0-20zm6.9 9h-3a15 15 0 0 0-1.3-5.6A8 8 0 0 1 18.9 11zM12 4.1c.9 1.2 1.8 3.6 1.9 6.9h-3.8c.1-3.3 1-5.7 1.9-6.9zM9.4 5.4A15 15 0 0 0 8.1 11h-3a8 8 0 0 1 4.3-5.6zM5.1 13h3a15 15 0 0 0 1.3 5.6A8 8 0 0 1 5.1 13zm6.9 6.9c-.9-1.2-1.8-3.6-1.9-6.9h3.8c-.1 3.3-1 5.7-1.9 6.9zm2.6-1.3a15 15 0 0 0 1.3-5.6h3a8 8 0 0 1-4.3 5.6z"/></svg>
        <span>www.<span class="accent">harlowandreed</span>.ca</span>
      </li>
    </ul>

    <div class="back__city">Calgary, AB</div>

    <div class="wordmark back__wordmark">Harlow &amp; Reed</div>

    <div class="back__band"></div>
    <div class="back__band-accent" role="img" aria-label="Row of three small maple leaf emblems"></div>

    <div class="back__tagline">Gifts from our best, to your best</div>
    <div class="social">
      <span class="social__badge" role="img" aria-label="Social network badge"></span>
      <span class="social__badge" role="img" aria-label="Social network badge"></span>
    </div>
  </section>
</body>
</html>
```